Veltrix4 Business Card - Health

Veltrix4 maximizes value from the health data of its clients, including doctors, HMOs, and patients. I have attached the Veltrix4 logo as an ai and eps file.
Target Market(s)
Health, HMO, Healthcare, Data, Big Data, Data Analytics
Industry/Entity Type
Business
Requirements
Must have
- At least one side should have some white on it so that we can write on it.

```html
<!DOCTYPE html>
<html lang="en">
<head>
<meta charset="utf-8">
<title>Veltrix4 Business Card</title>
<link rel="stylesheet" href="https://fonts.googleapis.com/css2?family=Arimo:wght@400;700&display=swap">
<style>
  :root {
    --backdrop: #1e1e20;
    --brand-blue: #0a6fd6;
    --brand-blue-light: #1c86ec;
    --brand-blue-deep: #0558b4;
    --paper: #ffffff;
    --paper-shade: #e4e4e4;
    --ink-grey: #4a4a4a;
    --divider: #1a1a1a;
    --text-light: #ffffff;
  }
  * { margin: 0; padding: 0; box-sizing: border-box; }
  html, body { width: 1200px; height: 871px; overflow: hidden; }
  body {
    background: var(--backdrop);
    font-family: "Arimo", Arial, sans-serif;
    display: flex;
    flex-direction: column;
    align-items: center;
    justify-content: center;
    gap: 56px;
  }
  .card {
    width: 525px;
    height: 300px;
    position: relative;
    overflow: hidden;
  }

  /* Back side */
  .card-back {
    background: linear-gradient(120deg, var(--brand-blue-light) 0%, var(--brand-blue) 55%, var(--brand-blue-deep) 100%);
    display: flex;
    align-items: flex-end;
    justify-content: center;
    padding-bottom: 48px;
  }
  .card-back .web-address {
    color: var(--text-light);
    opacity: 0.75;
    font-size: 12px;
    letter-spacing: 5px;
  }

  /* Front side */
  .card-front { display: flex; }
  .contact-panel {
    width: 46%;
    background: radial-gradient(circle at 45% 20%, var(--brand-blue-light), var(--brand-blue) 60%, var(--brand-blue-deep));
    color: var(--text-light);
    padding: 38px 0 0 32px;
    border-right: 2px solid var(--divider);
  }
  .person-name { font-size: 19px; font-weight: 700; margin-left: 18px; }
  .person-role { font-size: 13px; margin: 2px 0 0 18px; }
  .address { font-size: 12.5px; line-height: 1.35; margin: 28px 0 6px 10px; }
  .contact-list { list-style: none; font-size: 12.5px; }
  .contact-list li { display: flex; align-items: center; gap: 8px; height: 19px; }
  .contact-list svg { width: 13px; height: 13px; fill: var(--text-light); flex: none; }

  .brand-panel {
    flex: 1;
    background: linear-gradient(160deg, var(--paper) 40%, var(--paper-shade) 100%);
    display: flex;
    align-items: center;
    justify-content: center;
    gap: 14px;
  }
  .brand-dot { width: 38px; height: 38px; border-radius: 50%; background: var(--brand-blue); }
  .brand-name { font-size: 42px; font-weight: 400; color: var(--ink-grey); }
</style>
</head>
<body>
  <section class="card card-back" aria-label="Card back">
    <span class="web-address">www.veltrix4.net</span>
  </section>

  <section class="card card-front" aria-label="Card front">
    <div class="contact-panel">
      <p class="person-name">Mara Quell</p>
      <p class="person-role">President</p>
      <p class="address">2719 Harborview Lane<br>Ashford Bay, OR 97010</p>
      <ul class="contact-list">
        <li><svg viewBox="0 0 16 16"><path d="M3 2h3l1 4-2 1a9 9 0 0 0 4 4l1-2 4 1v3c0 1-1 1-2 1A12 12 0 0 1 2 4c0-1 0-2 1-2z"/></svg>555 0142 7781</li>
        <li><svg viewBox="0 0 16 16"><path d="M5 1h6a1 1 0 0 1 1 1v12a1 1 0 0 1-1 1H5a1 1 0 0 1-1-1V2a1 1 0 0 1 1-1zm1 2v8h4V3z"/></svg>555 0193 4406</li>
        <li><svg viewBox="0 0 16 16"><path d="M4 2h7v3H4zM2 6h12v6h-2v2H4v-2H2zm3 4v2h6v-2z"/></svg>555 0167 2259</li>
        <li><svg viewBox="0 0 16 16"><path d="M1 4h14v9H1zm1 1v1l6 4 6-4V5z"/></svg>mara@veltrix4.net</li>
        <li><svg viewBox="0 0 16 16"><circle cx="8" cy="8" r="7"/></svg>www.veltrix4.net</li>
      </ul>
    </div>
    <div class="brand-panel">
      <span class="brand-dot"></span>
      <span class="brand-name">Veltrix4</span>
    </div>
  </section>
</body>
</html>
```